stationary deign for trucking company

im a trucking company looking for a professional set of stationary designs i deliver goods from point a to b
Updates

When submitting stationary designs I need envelope design, letterhead, cards, I’d badge etc

Industry/Entity Type

Trucking Company

Requirements
Must have
• must have letter head, business card, envelope, fax sheet, id badge, folder, thank you card, notebook, invoice sheet.
Nice to have
• nice to have them all custom made (letterhead,envelope, business card, I’d badge etc
Should not have
• must not have prepaid sign want i unique design for items

```html
<!DOCTYPE html>
<html lang="en">
<head>
<meta charset="utf-8">
<title>Harlow Transportation + Logistics — Stationery Set</title>
<link href="https://fonts.googleapis.com/css2?family=Montserrat:wght@500;600&family=Open+Sans:wght@400;600&display=swap" rel="stylesheet">
<style>
  :root{
    --backdrop:#c6c6c6;
    --paper:#ffffff;
    --paper-soft:#f9f9f9;
    --ink:#1d1d1f;
    --charcoal:#231f20;
    --brand-blue:#1e56a8;
    --band:#d1d2d4;
    --faint:#dfe3ec;
    --muted:#3a3a3a;
    --folder-text:#dddddd;
  }
  *{box-sizing:border-box;margin:0;padding:0}
  html,body{width:1200px;height:1200px;overflow:hidden}
  body{background:var(--backdrop);font-family:"Open Sans",Arial,sans-serif;color:var(--ink);position:relative}

  .sheet{position:absolute;background:var(--paper);box-shadow:0 2px 4px rgba(0,0,0,.25);overflow:hidden}

  .brand{position:absolute;display:flex;align-items:center;gap:10px}
  .brand__mark{background:var(--brand-blue);flex:none}
  .brand__text{display:flex;flex-direction:column}
  .brand__name{font-family:"Montserrat",Arial,sans-serif;font-weight:500;letter-spacing:.14em;line-height:1;color:var(--ink)}
  .brand__tag{font-family:"Montserrat",Arial,sans-serif;font-weight:600;letter-spacing:.2em;color:var(--ink);margin-top:3px;white-space:nowrap}

  .watermark{position:absolute;transform:translate(-50%,-50%);font-family:"Montserrat",Arial,sans-serif;font-weight:500;color:var(--faint);letter-spacing:.04em;line-height:1;white-space:nowrap}

  .footer{position:absolute;left:0;right:0;text-align:center;font-size:6.5px;color:var(--muted);line-height:1.5}
  .contact-row{display:inline-flex;align-items:center;gap:3px;margin:0 3px}
  .icon{display:inline-block;width:6px;height:6px;background:var(--brand-blue);border-radius:50%}
  .icon--mail{border-radius:1px;height:5px}
  .icon--phone{border-radius:1px 3px 1px 3px}

  .fax-table{position:absolute;left:14px;top:143px;width:414px}
  .fax-row{display:flex;background:var(--band);height:20px;margin-bottom:2px;align-items:center;font-size:8px}
  .fax-row span{width:50%}
  .fax-row span:first-child{padding-left:19px}
  .fax-checks{position:absolute;left:33px;top:239px;display:flex;gap:18px;font-size:8px}
  .fax-checks label{display:flex;align-items:center;gap:10px}
  .fax-checks i{width:10px;height:10px;border:1px solid #555;display:inline-block}

  .card--dark{background:var(--charcoal)}
  .card__person{position:absolute;left:18px;top:60px}
  .card__name{font-size:9px;font-weight:600;color:var(--brand-blue)}
  .card__title{font-size:6.5px}
  .card__info{position:absolute;left:18px;top:90px;font-size:5.5px;line-height:1.45}
  .card__info .contact-row{margin:0;display:flex}

  .envelope-info{position:absolute;left:18px;top:196px;font-size:7px;line-height:1.55}
  .envelope-info .contact-row{margin:0;display:flex;gap:6px}

  .folder-shell{position:absolute;left:0;top:685px}
  .folder-info{position:absolute;left:43px;top:1012px;font-size:5px;color:var(--folder-text);line-height:1.55}
  .folder-info .contact-row{margin:0;display:flex}
  .folder-info .icon{width:4px;height:4px}
</style>
</head>
<body>

<!-- Letterhead -->
<section class="sheet letterhead" style="left:30px;top:41px;width:444px;height:628px">
  <div class="brand" style="left:93px;top:36px">
    <span class="brand__mark" style="width:14px;height:14px"></span>
    <div class="brand__text">
      <span class="brand__name" style="font-size:28px">HARLOW</span>
      <span class="brand__tag" style="font-size:8px">TRANSPORTATION + LOGISTICS</span>
    </div>
  </div>
  <div class="watermark" style="left:230px;top:314px;font-size:52px">HARLOW</div>
  <div class="footer" style="top:590px">
    1275 Mill Creek Rd Suite 12 Brenham, TX 77833<br>
    <span class="contact-row"><i class="icon icon--phone"></i>+1 555.014.2260</span>
    <span class="contact-row"><i class="icon icon--mail"></i>info@harlowtl.com</span>
    <span class="contact-row"><i class="icon"></i>www.harlowtl.com</span>
  </div>
</section>

<!-- Fax sheet -->
<section class="sheet fax" style="left:493px;top:45px;width:442px;height:624px">
  <div class="brand" style="left:117px;top:28px">
    <span class="brand__mark" style="width:13px;height:13px"></span>
    <div class="brand__text">
      <span class="brand__name" style="font-size:24px">HARLOW</span>
      <span class="brand__tag" style="font-size:7px">TRANSPORTATION + LOGISTICS</span>
    </div>
  </div>
  <div class="fax-table">
    <div class="fax-row"><span>To</span><span>From</span></div>
    <div class="fax-row"><span>Fax</span><span>Pages</span></div>
    <div class="fax-row"><span>Phone</span><span>Date</span></div>
    <div class="fax-row"><span>Re</span><span>CC</span></div>
  </div>
  <div class="fax-checks">
    <label><i></i>Urgent</label>
    <label><i></i>For Review</label>
    <label><i></i>Please Comment</label>
    <label><i></i>Reply</label>
    <label><i></i>Recycle</label>
  </div>
  <div class="watermark" style="left:235px;top:378px;font-size:48px">HARLOW</div>
  <div class="footer" style="top:592px">
    1275 Mill Creek Rd Suite 12 Brenham, TX 77833<br>
    <span class="contact-row"><i class="icon icon--phone"></i>+1 555.014.2260</span>
    <span class="contact-row"><i class="icon icon--mail"></i>info@harlowtl.com</span>
    <span class="contact-row"><i class="icon"></i>www.harlowtl.com</span>
  </div>
</section>

<!-- Business card front -->
<section class="sheet card card--dark" style="left:872px;top:321px;width:260px;height:156px">
  <div class="brand" style="left:72px;top:62px">
    <span class="brand__mark" style="width:14px;height:14px"></span>
    <span class="brand__name" style="font-size:26px;color:#ffffff">HARLOW</span>
  </div>
</section>

<!-- Business card back -->
<section class="sheet card" style="left:872px;top:493px;width:260px;height:155px">
  <div class="brand" style="left:20px;top:22px;gap:6px">
    <span class="brand__mark" style="width:8px;height:8px"></span>
    <div class="brand__text">
      <span class="brand__name" style="font-size:13px">HARLOW</span>
      <span class="brand__tag" style="font-size:4px;margin-top:2px">TRANSPORTATION + LOGISTICS</span>
    </div>
  </div>
  <div class="watermark" style="left:200px;top:80px;font-size:22px">HARLOW</div>
  <div class="card__person">
    <div class="card__name">Dana Whitfield</div>
    <div class="card__title">Chief Executive</div>
  </div>
  <div class="card__info">
    Northgate Business Centre<br>
    410 Cedar Row, Riverton, BC Canada
    <div style="height:5px"></div>
    <span class="contact-row"><i class="icon icon--phone"></i>&nbsp;+1 555.014.2260</span>
    <span class="contact-row"><i class="icon icon--mail"></i>&nbsp;info@harlowtl.com</span>
    <span class="contact-row"><i class="icon"></i>&nbsp;www.harlowtl.com</span>
  </div>
</section>

<!-- Presentation folder -->
<svg class="folder-shell" width="620" height="500" viewBox="0 0 620 500" aria-hidden="true">
  <path d="M29 0 H307 V371 Q302 430 298 458 Q292 496 255 496 H29 Z" fill="#231f20"/>
  <path d="M29 247 L2 262 V370 L29 385 Z" fill="#231f20"/>
  <rect x="307" y="0" width="279" height="371" fill="#ffffff"/>
  <path d="M586 247 L613 262 V360 L586 375 Z" fill="#231f20"/>
  <path d="M311 371 H586 V496 H352 Q318 496 315 460 Z" fill="#231f20"/>
</svg>
<div class="brand" style="left:347px;top:722px;gap:8px">
  <span class="brand__mark" style="width:12px;height:12px"></span>
  <div class="brand__text">
    <span class="brand__name" style="font-size:24px">HARLOW</span>
    <span class="brand__tag" style="font-size:7px">TRANSPORTATION + LOGISTICS</span>
  </div>
</div>
<div class="watermark" style="left:447px;top:924px;font-size:42px">HARLOW</div>
<div class="folder-info">
  1275 Mill Creek Rd Suite 12 Brenham, TX 77833
  <span class="contact-row"><i class="icon icon--phone"></i>&nbsp;+1 555.014.2260</span>
  <span class="contact-row"><i class="icon icon--mail"></i>&nbsp;info@harlowtl.com</span>
  <span class="contact-row"><i class="icon"></i>&nbsp;www.harlowtl.com</span>
</div>

<!-- Envelope -->
<svg style="position:absolute;left:644px;top:685px" width="536" height="72" viewBox="0 0 536 72" aria-hidden="true">
  <path d="M0 72 L18 14 Q22 0 38 0 H498 Q514 0 518 14 L536 72 Z" fill="#231f20"/>
</svg>
<section class="sheet envelope" style="left:644px;top:756px;width:536px;height:254px;background:var(--paper-soft)">
  <div class="brand" style="left:20px;top:22px;gap:8px">
    <span class="brand__mark" style="width:12px;height:12px"></span>
    <div class="brand__text">
      <span class="brand__name" style="font-size:22px">HARLOW</span>
      <span class="brand__tag" style="font-size:6.5px">TRANSPORTATION + LOGISTICS</span>
    </div>
  </div>
  <div class="watermark" style="left:410px;top:124px;font-size:46px">HARLOW</div>
  <div class="envelope-info">
    1275 Mill Creek Rd Suite 12 Brenham, TX 77833
    <span class="contact-row"><i class="icon icon--phone"></i>+1 555.014.2260</span>
    <span class="contact-row"><i class="icon icon--mail"></i>info@harlowtl.com</span>
    <span class="contact-row"><i class="icon"></i>www.harlowtl.com</span>
  </div>
</section>

</body>
</html>
```